Online Course Page

We are building a video based online course page. This project is for only the actual page that the student will watch the videos at. They will watch one vide at a time. Once one video lesson is completed then they can move to the next video lesson. The page will need to show the video player. (Main feature.) The list of lessons in the course. Instructor information. Profile picture and bio of the instructor. A Live chat button that will initiate a chat in real-time with the instructor.

The winning designer will also be asked to to design the dashboard area and other aspects of the user interface as an additional project.

Target Market(s)

Adults

Number of Pages Required

1 page

Colors
9bcb3c

Requirements
Must have
• Our logo is attached. Green and grey are our colors. Should feel modern, clean and be simple to navigate. The site will be responsive so the layout should work well on mobile devices.

```html
<!DOCTYPE html>
<html lang="en">
<head>
<meta charset="utf-8">
<title>CSS Grid Layout – LearnHarbor</title>
<link rel="stylesheet" href="https://fonts.googleapis.com/css2?family=Roboto:wght@400;500;700&display=swap">
<style>
:root{
  --green:#9bcb3c;
  --green-dark:#7db02a;
  --page:#f2f2f2;
  --card:#f8f8f8;
  --header:#fafafa;
  --ink:#3c3c3c;
  --body:#555;
  --link:#2f6aa8;
  --line:#dcdcdc;
  --muted:#a9a9a9;
  --video-a:#02134a;
  --video-b:#0a2a8c;
}
*{box-sizing:border-box;margin:0;padding:0}
html,body{width:851px;height:1200px;overflow:hidden}
body{background:var(--page);font-family:"Roboto",sans-serif;color:var(--ink);position:relative}
.site-header{position:absolute;left:0;top:0;width:851px;height:53px;background:var(--header);border-bottom:1px solid #e2e2e2}
.brand{position:absolute;left:53px;top:15px;display:flex;align-items:center;gap:6px;font-weight:700;font-size:16px;color:var(--ink)}
.brand-dot{width:14px;height:14px;border-radius:50%;background:var(--green)}
.search{position:absolute;left:181px;top:12px;width:233px;height:26px;background:#eeeeee;border-radius:3px;font-size:10.5px;color:#999;padding:7px 12px}
.search svg{position:absolute;right:12px;top:6px}
.nav-item{position:absolute;top:19px;font-size:11px;color:#444;display:flex;align-items:center;gap:4px}
.account{position:absolute;left:760px;top:13px;display:flex;align-items:center;gap:4px}
.page-title{position:absolute;left:53px;top:74px;font-size:21px;font-weight:500;color:#444}
.player{position:absolute;left:53px;top:125px;width:745px;height:458px;background:#fff;box-shadow:0 1px 3px rgba(0,0,0,.12)}
.video{position:absolute;left:0;top:0;width:745px;height:419px;background:linear-gradient(120deg,var(--video-a),var(--video-b) 55%,#061a66)}
.controls{position:absolute;left:0;bottom:0;width:100%;height:27px;background:rgba(0,5,30,.55)}
.progress{position:absolute;left:19px;top:-2px;width:706px;height:3px;background:#666}
.progress span{display:block;width:249px;height:100%;background:var(--green)}
.play{position:absolute;left:26px;top:8px}
.time{position:absolute;left:60px;top:8px;font-size:10px;color:#fff}
.fullscreen{position:absolute;right:26px;top:7px}
.next-lesson{position:absolute;right:22px;top:434px;font-size:10.5px;font-weight:500;color:var(--green-dark);display:flex;align-items:center;gap:4px}
.course-card{position:absolute;left:53px;top:606px;width:491px;height:543px;background:var(--card);box-shadow:0 1px 3px rgba(0,0,0,.12);padding:19px 12px}
.card-title{font-size:14.5px;font-weight:500;color:#444}
.about p{margin-top:8px;font-size:10.3px;line-height:17px;color:var(--body);padding-right:4px}
.section-title{margin-top:45px;margin-bottom:13px}
.section-title.second{margin-top:25px}
.lessons{list-style:none;border-top:1px solid var(--line)}
.lesson{height:33px;border-bottom:1px solid var(--line);display:flex;align-items:center;padding:0 13px 0 13px;font-size:10.3px}
.lesson.active{background:#efefef}
.lesson-name{color:var(--link);flex:1}
.lesson-time{color:#555;width:40px}
.lessons.first .lesson:last-child{height:39px}
.instructor-card{position:absolute;left:563px;top:606px;width:235px;height:315px;background:var(--card);box-shadow:0 1px 3px rgba(0,0,0,.12);padding:12px 11px}
.instructor-card .card-title{font-size:12px}
.portrait{position:absolute;left:12px;top:40px;width:82px;height:82px;border-radius:50%;background:radial-gradient(circle at 50% 40%,#b08a72,#3e3a3a 70%)}
.instructor-name{position:absolute;left:113px;top:51px;font-size:10.5px;color:#555}
.chat-btn{position:absolute;left:113px;top:76px;width:94px;height:25px;background:var(--green);border-radius:2px;color:#fff;font-size:10.3px;font-weight:500;display:flex;align-items:center;justify-content:center;gap:6px}
.bio{position:absolute;left:12px;top:146px;width:212px;font-size:10.2px;line-height:13px;color:var(--body)}
.show-more{position:absolute;left:12px;top:266px;font-size:10.3px;font-weight:500;color:#444;display:flex;align-items:center;gap:4px}
</style>
</head>
<body>
<header class="site-header">
  <div class="brand"><span class="brand-dot"></span>LearnHarbor</div>
  <div class="search">Search for courses
    <svg width="12" height="12" viewBox="0 0 12 12"><circle cx="5" cy="5" r="3.8" fill="none" stroke="#9bcb3c" stroke-width="1.5"/><line x1="8" y1="8" x2="11" y2="11" stroke="#9bcb3c" stroke-width="1.5"/></svg>
  </div>
  <div class="nav-item" style="left:435px">Courses <svg width="8" height="6" viewBox="0 0 8 6"><path d="M1 1l3 3 3-3" fill="none" stroke="#444" stroke-width="1.1"/></svg></div>
  <div class="nav-item" style="left:504px">Catergories <svg width="8" height="6" viewBox="0 0 8 6"><path d="M1 1l3 3 3-3" fill="none" stroke="#444" stroke-width="1.1"/></svg></div>
  <div class="account">
    <svg width="27" height="27" viewBox="0 0 27 27"><circle cx="13.5" cy="13.5" r="12.5" fill="#f4f4f4" stroke="#888" stroke-width="1.2"/><circle cx="13.5" cy="10.5" r="4.5" fill="#bbb"/><path d="M5.5 21.5c2-4 5-5.5 8-5.5s6 1.5 8 5.5" fill="#bbb"/></svg>
    <svg width="8" height="6" viewBox="0 0 8 6"><path d="M1 1l3 3 3-3" fill="none" stroke="#444" stroke-width="1.1"/></svg>
  </div>
</header>

<h1 class="page-title">CSS Grid Layout</h1>

<section class="player">
  <div class="video" role="img" aria-label="Lesson video frame showing CSS code on a dark blue screen"></div>
  <div class="controls" style="top:392px;height:27px">
    <div class="progress"><span></span></div>
    <svg class="play" width="9" height="12" viewBox="0 0 9 12"><path d="M0 0l9 6-9 6z" fill="#fff"/></svg>
    <span class="time">1:34/4:44</span>
    <svg class="fullscreen" width="14" height="14" viewBox="0 0 14 14" fill="none" stroke="#fff" stroke-width="1.3"><path d="M1 4V1h3M10 1h3v3M13 10v3h-3M4 13H1v-3"/><rect x="4" y="4" width="6" height="6"/></svg>
  </div>
  <div class="next-lesson">Next Lesson <svg width="5" height="8" viewBox="0 0 5 8"><path d="M1 1l3 3-3 3" fill="none" stroke="#7db02a" stroke-width="1.2"/></svg></div>
</section>

<main class="course-card">
  <div class="about">
    <h2 class="card-title">About the course.</h2>
    <p>Lorem ipsum dolor sit amet, consectetur adipiscing elit. In aliquam nisi vel elit consectetur vehicula. In enim tellus, efficitur at tristique vehicula, gravida vitae sem. Morbi eu pulvinar lectus. Curabitur quam odio, vehicula varius luctus ut, mattis nec purus.</p>
  </div>

  <h2 class="card-title section-title">Introducing Grid Layout</h2>
  <ul class="lessons first">
    <li class="lesson"><span class="lesson-name">Understanding Grid</span><span class="lesson-time">3:21</span><svg width="17" height="17" viewBox="0 0 17 17"><circle cx="8.5" cy="8.5" r="7.5" fill="none" stroke="#aaa"/><path d="M7 5.5l4 3-4 3z" fill="#aaa"/></svg></li>
    <li class="lesson active"><span class="lesson-name">Grid Concepts and Terminology</span><span class="lesson-time">2.:31</span><svg width="17" height="17" viewBox="0 0 17 17"><circle cx="8.5" cy="8.5" r="7.5" fill="none" stroke="#aaa"/><path d="M7 5.5l4 3-4 3z" fill="#aaa"/></svg></li>
    <li class="lesson"><span class="lesson-name">Defining a Gid</span><span class="lesson-time">4:55</span><svg width="17" height="17" viewBox="0 0 17 17"><circle cx="8.5" cy="8.5" r="7.5" fill="none" stroke="#aaa"/><path d="M7 5.5l4 3-4 3z" fill="#aaa"/></svg></li>
    <li class="lesson"><span class="lesson-name">Setting Grid Rows</span><span class="lesson-time">5:23</span><svg width="17" height="17" viewBox="0 0 17 17"><circle cx="8.5" cy="8.5" r="7.5" fill="none" stroke="#aaa"/><path d="M7 5.5l4 3-4 3z" fill="#aaa"/></svg></li>
    <li class="lesson"><span class="lesson-name">Add Gutters Between Rows and Columns</span><span class="lesson-time">4:33</span><svg width="17" height="17" viewBox="0 0 17 17"><circle cx="8.5" cy="8.5" r="7.5" fill="none" stroke="#aaa"/><path d="M7 5.5l4 3-4 3z" fill="#aaa"/></svg></li>
  </ul>

  <h2 class="card-title section-title second">Flexible Sized Grids</h2>
  <ul class="lessons">
    <li class="lesson"><span class="lesson-name">Flexible Tracks</span><span class="lesson-time">3:21</span><svg width="17" height="17" viewBox="0 0 17 17"><circle cx="8.5" cy="8.5" r="7.5" fill="none" stroke="#aaa"/><path d="M7 5.5l4 3-4 3z" fill="#aaa"/></svg></li>
    <li class="lesson"><span class="lesson-name">Set Tracks with repeat() Notation</span><span class="lesson-time">2.:31</span><svg width="17" height="17" viewBox="0 0 17 17"><circle cx="8.5" cy="8.5" r="7.5" fill="none" stroke="#aaa"/><path d="M7 5.5l4 3-4 3z" fill="#aaa"/></svg></li>
    <li class="lesson"><span class="lesson-name">Auto-generate Flexible Columns</span><span class="lesson-time">4:55</span><svg width="17" height="17" viewBox="0 0 17 17"><circle cx="8.5" cy="8.5" r="7.5" fill="none" stroke="#aaa"/><path d="M7 5.5l4 3-4 3z" fill="#aaa"/></svg></li>
  </ul>
</main>

<aside class="instructor-card">
  <h2 class="card-title">Instructor</h2>
  <div class="portrait" role="img" aria-label="Instructor profile photo"></div>
  <div class="instructor-name">Daniel Marlow</div>
  <div class="chat-btn">
    <svg width="15" height="13" viewBox="0 0 15 13"><path d="M1.5 1h12v8h-8l-3 3v-3h-1z" fill="none" stroke="#fff" stroke-width="1.2" stroke-linejoin="round"/></svg>
    Live Chat
  </div>
  <p class="bio">Lorem ipsum dolor sit amet, consectetur adipiscing elit. In aliquam nisi vel elit consectetur vehicula. In enim tellus, efficitur at tristique vehicula, gravida vitae sem. Morbi eu pulvinar lectus. Curabitur quam odio, vehicula varius luctus ut, mattis nec purus. Nam elementum nibh vel nisl fermentum rhoncus.</p>
  <div class="show-more">Show More <svg width="5" height="8" viewBox="0 0 5 8"><path d="M1 1l3 3-3 3" fill="none" stroke="#444" stroke-width="1.2"/></svg></div>
</aside>
</body>
</html>
```